I am A local real estate investor in the highly competitive single family homes market of Austin,Tx.for fix and flipping My company uses several nontraditional and creative solutions for helping home owners sell their faster for cash with a closing date of their choice and helps them save thousands of dollars in having to pay real estate commissions and fees.My idea for the front of the postcard is to show the home owner what they could do with all the money they'll save by selling their home with us.I want a background picture on the front of taking a vacation with the money they'll save, or down payment on a new car on the back or even just a pile of cash they'll save to do whatever they like with.
Company name: Bold Harbor Properties
website: www.Velmorquickdeal.com
phone # : 512-874-2296 / 24hr.recorded message

```html
<!DOCTYPE html>
<html lang="en">
<head>
<meta charset="utf-8">
<title>Bold Harbor Properties – Sell Your Home With Us</title>
<link href="https://fonts.googleapis.com/css2?family=Open+Sans:wght@400;600;700;800&family=Oswald:wght@400;500&display=swap" rel="stylesheet">
<style>
  :root{
    --red:#d3212c;
    --blue:#1b5aa3;
    --blue-dark:#15467f;
    --ink:#1f2430;
    --white:#ffffff;
    --rule:#c9ced6;
  }
  *{margin:0;padding:0;box-sizing:border-box}
  html,body{width:1200px;height:811px;overflow:hidden;background:var(--white)}
  .postcard{position:relative;width:1200px;height:811px;overflow:hidden;background:var(--white);font-family:"Open Sans",Arial,sans-serif;color:var(--ink)}
  .backdrop{position:absolute;inset:0}
  .brand{position:absolute;left:52px;top:112px;display:flex;align-items:center;gap:10px;width:240px}
  .brand-mark{width:18px;height:18px;background:var(--red);flex:none}
  .brand-name{font-weight:700;font-size:25px;line-height:1.1;color:var(--blue)}
  .hero-photo{position:absolute;left:30px;top:60px;width:650px;height:560px;
    background:radial-gradient(ellipse at 50% 35%,#e9d7c8 0%,#d9dde4 45%,#eef1f5 80%);border-radius:4px}
  .headline{position:absolute;left:696px;top:52px;width:470px}
  .headline-sell{font-weight:800;font-size:178px;line-height:1;letter-spacing:-2px;color:var(--red)}
  .headline-home{font-weight:700;font-size:38px;line-height:1;color:var(--blue);margin-top:-2px;white-space:nowrap}
  .rule{height:1.5px;background:var(--rule);margin:10px 0 11px}
  .headline-save{font-weight:800;font-size:45px;line-height:1;color:var(--red);white-space:nowrap}
  .headline-fees{font-weight:700;font-size:27px;line-height:1.2;color:var(--blue);margin-top:4px}
  .intro{position:absolute;left:698px;top:378px;width:450px;font-size:19px;line-height:1.3;color:var(--ink)}
  .offer-badge{position:absolute;left:694px;top:472px;width:92px;height:92px;border-radius:50%;
    background:var(--blue);border:4px solid var(--white);box-shadow:0 0 0 1px var(--rule);
    display:flex;align-items:center;justify-content:center;color:var(--white);font-weight:800;font-size:29px;z-index:3}
  .offer-ribbon{position:absolute;left:770px;top:494px;width:230px;height:58px;z-index:2;
    color:var(--white);font-weight:800;font-size:22px;line-height:1.05;text-align:center;padding-top:6px}
  .offer-ribbon svg{position:absolute;inset:0;z-index:-1}
  .benefits{position:absolute;left:688px;top:526px;width:512px;height:210px;background:var(--white);
    border-left:2px solid var(--red);box-shadow:0 2px 6px rgba(0,0,0,.25);padding:50px 0 0 68px;list-style:none}
  .benefits li{display:flex;align-items:center;gap:9px;font-size:17.5px;height:32.5px;color:var(--ink)}
  .benefits svg{flex:none}
  .call-label{position:absolute;left:100px;top:632px;width:500px;display:flex;align-items:center;gap:14px;
    font-family:"Oswald",Arial,sans-serif;font-size:27px;color:var(--white);letter-spacing:.5px}
  .call-label::before,.call-label::after{content:"";flex:1;height:1.5px;background:var(--red)}
  .phone{position:absolute;left:92px;top:668px;display:flex;align-items:center;gap:14px}
  .phone-number{font-family:"Oswald",Arial,sans-serif;font-weight:500;font-size:62px;line-height:1;color:var(--white);letter-spacing:1px}
  .hotline{position:relative;width:78px;height:60px;margin-left:6px;text-align:center;color:var(--white)}
  .hotline-hours{font-family:"Oswald",Arial,sans-serif;font-weight:500;font-size:30px;line-height:1}
  .hotline-note{display:inline-block;background:var(--white);color:var(--blue);font-weight:800;font-size:7.5px;
    padding:2px 4px;border-radius:8px;transform:rotate(-12deg);margin-top:-4px;white-space:nowrap}
  .website{position:absolute;left:164px;top:750px;font-size:15px;color:var(--white)}
  .website a{color:var(--red);font-weight:700;text-decoration:none;margin-left:6px}
  .cta{position:absolute;right:44px;top:755px;font-size:23px;color:var(--white)}
</style>
</head>
<body>
<div class="postcard">
  <svg class="backdrop" width="1200" height="811" viewBox="0 0 1200 811" aria-hidden="true">
    <path d="M0 612 Q340 596 688 598 L688 736 L1200 736 L1200 811 L0 811 Z" fill="var(--red)"/>
    <path d="M0 622 Q340 606 688 606 L688 736 L1200 736 L1200 811 L0 811 Z" fill="var(--blue)"/>
  </svg>

  <div class="hero-photo" role="img" aria-label="Smiling businessman in shirt and tie holding up stacks of cash in both hands"></div>

  <div class="brand">
    <span class="brand-mark"></span>
    <span class="brand-name">Bold Harbor Properties</span>
  </div>

  <div class="headline">
    <div class="headline-sell">SELL</div>
    <div class="headline-home">YOUR HOME WITH US!</div>
    <div class="rule"></div>
    <div class="headline-save">SAVE THOUSANDS</div>
    <div class="headline-fees">in Commissions and Fees</div>
    <div class="rule" style="margin-top:6px"></div>
  </div>

  <p class="intro">Did you know there are at least a 12 Different Ways to Sell Your Property that Realtors won't tell you about?</p>

  <div class="offer-badge">100%</div>
  <div class="offer-ribbon">
    <svg width="230" height="58" viewBox="0 0 230 58" aria-hidden="true">
      <path d="M0 0 H230 L218 58 H0 Z" fill="var(--red)"/>
    </svg>
    GUARANTEED<br>CASH OFFER
  </div>
  <svg style="position:absolute;left:998px;top:520px" width="202" height="6" aria-hidden="true"><rect width="202" height="2" y="2" fill="var(--red)"/></svg>

  <ul class="benefits">
    <li><svg width="14" height="14" viewBox="0 0 14 14"><rect x="1" y="2" width="10" height="10" fill="none" stroke="var(--red)" stroke-width="1.4"/><path d="M3.5 6.5 L6 9 L12.5 1.5" fill="none" stroke="var(--red)" stroke-width="2"/></svg>We Buy Properties Fast</li>
    <li><svg width="14" height="14" viewBox="0 0 14 14"><rect x="1" y="2" width="10" height="10" fill="none" stroke="var(--red)" stroke-width="1.4"/><path d="M3.5 6.5 L6 9 L12.5 1.5" fill="none" stroke="var(--red)" stroke-width="2"/></svg>We buy with cash</li>
    <li><svg width="14" height="14" viewBox="0 0 14 14"><rect x="1" y="2" width="10" height="10" fill="none" stroke="var(--red)" stroke-width="1.4"/><path d="M3.5 6.5 L6 9 L12.5 1.5" fill="none" stroke="var(--red)" stroke-width="2"/></svg>We have many creative solutions available</li>
    <li><svg width="14" height="14" viewBox="0 0 14 14"><rect x="1" y="2" width="10" height="10" fill="none" stroke="var(--red)" stroke-width="1.4"/><path d="M3.5 6.5 L6 9 L12.5 1.5" fill="none" stroke="var(--red)" stroke-width="2"/></svg>Choose your closing Date</li>
    <li><svg width="14" height="14" viewBox="0 0 14 14"><rect x="1" y="2" width="10" height="10" fill="none" stroke="var(--red)" stroke-width="1.4"/><path d="M3.5 6.5 L6 9 L12.5 1.5" fill="none" stroke="var(--red)" stroke-width="2"/></svg>We buy as is .. No repairs necessary</li>
  </ul>

  <div class="call-label">CALL US AT:</div>
  <div class="phone">
    <svg width="38" height="38" viewBox="0 0 24 24" aria-hidden="true">
      <path d="M6.6 10.8c1.4 2.8 3.8 5.1 6.6 6.6l2.2-2.2c.3-.3.7-.4 1-.2 1.1.4 2.3.6 3.6.6.6 0 1 .4 1 1V20c0 .6-.4 1-1 1C10.6 21 3 13.4 3 4c0-.6.4-1 1-1h3.5c.6 0 1 .4 1 1 0 1.3.2 2.5.6 3.6.1.3 0 .7-.2 1z" fill="var(--white)"/>
      <path d="M15 3a6 6 0 0 1 6 6M15 6a3 3 0 0 1 3 3" fill="none" stroke="var(--white)" stroke-width="1.6"/>
    </svg>
    <span class="phone-number">512-874-2296</span>
    <div class="hotline">
      <div class="hotline-hours">24/7</div>
      <span class="hotline-note">RECORDED MESSAGE</span>
    </div>
  </div>
  <p class="website">or visit out website: <a href="#">www.Velmorquickdeal.com</a></p>
  <p class="cta">Let Us Know How We Can Help!</p>
</div>
</body>
</html>
```